drink bottle label

Our drink is called VELMORA zi, a 2000 year old Asian formula for a fermented green tea drink. Flavored with organic ginger juice, cinnamon and lime. Very tasty and refreshing, good for sports recovery, digestion,liver detox,overall health and vitality. Naturally fermented creating a- no sugar, low GI, salt,-fat and gluten free- fizzy drink alternative to soft drink, sports drinks or beer. The bottle is a brown 330ml long neck bottle. For the diet and health conscious individual. We would like the label to be upmarket for restaurants & trendy organic food suppliers.
Updates

Reason: Take more time to get the best result

The bottle is brown. Try using black-gold-silver-white for the subject in a white or silver border

Target Market(s)

Upmarket, for restaurant & trendy organic food supplies.Sophisticated Health conscious people who don't want high sugar, caffeine drinks.

Industry/Entity Type

Health

Requirements
Must have
• The drink name and registered brand is" VELMORA zi."
Must feature PROBIOTICS & ENZYMES for detox.No artificial preservatives or colours. 100% Organic & raw living culture.Low GI low calorie- no cane sugar, no salt-
- no lactose, Coeliac -diabetic & vegan friendly. Ginger Brew.
Nice to have
• tastes great-revitalize- 330ml brown bottle

```html
<!DOCTYPE html>
<html lang="en">
<head>
<meta charset="utf-8">
<title>VELMORA zi – Ginger Brew Label</title>
<link rel="stylesheet" href="https://fonts.googleapis.com/css2?family=Montserrat:wght@600;700;800&family=Quicksand:wght@400&family=Fira+Sans:ital,wght@0,600;1,400;1,600;1,800&display=swap">
<style>
  :root {
    --backdrop: #e6e7e9;
    --silver-light: #f2f3f4;
    --silver-mid: #c9cbce;
    --silver-dark: #a7a9ad;
    --green-bright: #3fd83a;
    --green-mid: #20b81c;
    --green-deep: #0a8a12;
    --panel-white: #f7f8f7;
    --band-dark: #2b2725;
    --ink: #2a2a2a;
    --white: #ffffff;
    --rule-grey: #bdbdbd;
    --icon-dark: #2d2d2d;
  }
  * { box-sizing: border-box; margin: 0; padding: 0; }
  html, body { width: 1200px; height: 1000px; overflow: hidden; }
  body { background: var(--backdrop); position: relative; }

  .label {
    position: absolute; left: 266px; top: 120px;
    width: 668px; height: 762px;
    box-shadow: 0 6px 24px rgba(0,0,0,.18);
    overflow: hidden;
  }

  /* top flavour zone */
  .flavour-zone {
    position: absolute; left: 0; top: 0; width: 100%; height: 300px;
    background: linear-gradient(90deg, var(--silver-mid), var(--silver-light) 40%, var(--silver-mid));
  }
  .flavour-zone__green {
    position: absolute; left: 60px; top: 0; width: 548px; height: 100%;
    background:
      linear-gradient(90deg, transparent 0 12%, rgba(255,255,255,.18) 14% 18%, transparent 22% 70%, rgba(255,255,255,.15) 74% 80%, transparent 84%),
      linear-gradient(180deg, var(--green-mid), var(--green-bright) 55%, var(--green-mid));
  }
  .flavour-panel {
    position: absolute; left: 135px; top: 35px; width: 397px; height: 243px;
    background: var(--panel-white);
    text-align: center;
  }
  .flavour-panel__claim {
    margin-top: 14px;
    font: 800 17px/1 "Montserrat", sans-serif;
    color: var(--ink); letter-spacing: .2px;
  }
  .flavour-panel__name {
    margin: 12px auto 0; width: 383px; height: 110px;
    background: var(--green-deep);
    border: 3px solid var(--green-mid);
    display: flex; align-items: center; justify-content: center;
    font: 400 52px/1 "Quicksand", sans-serif; color: var(--white);
  }
  .flavour-panel__desc {
    margin-top: 12px;
    font: italic 600 23px/1.25 "Fira Sans", sans-serif;
    color: var(--ink);
  }

  /* brand band */
  .brand-band {
    position: absolute; left: 0; top: 300px; width: 100%; height: 228px;
    background: var(--band-dark);
  }
  .brand-band__name {
    position: absolute; left: 0; right: 0; top: 42px;
    text-align: center;
    font: 700 88px/1 "Montserrat", sans-serif;
    color: var(--white); letter-spacing: 2px;
  }
  .brand-band__sub {
    position: absolute; left: 0; right: 0; top: 148px; height: 44px;
    text-align: center;
    font: 700 44px/44px "Montserrat", sans-serif;
    color: var(--white);
  }
  .brand-band__rule {
    position: absolute; top: 170px; height: 2px; background: var(--rule-grey);
  }
  .brand-band__rule--left { left: 37px; width: 222px; }
  .brand-band__rule--right { left: 396px; width: 238px; }

  /* info zone */
  .info-zone {
    position: absolute; left: 0; top: 528px; width: 100%; height: 234px;
    background: linear-gradient(90deg, var(--silver-dark) 0 60px, var(--silver-light) 60px 608px, var(--silver-dark) 608px);
  }
  .info-zone__center {
    position: absolute; left: 60px; top: 0; width: 548px; height: 100%;
    background: linear-gradient(180deg, #fafafa, #ececec);
  }
  .badge-row {
    position: absolute; left: 88px; top: 34px;
    display: flex; align-items: center; gap: 8px;
  }
  .badge-row__group-label {
    writing-mode: vertical-rl; transform: rotate(180deg);
    font: 800 27px/1 "Montserrat", sans-serif; color: var(--ink);
    height: 62px; text-align: center;
  }
  .badge-row__divider { width: 2px; height: 70px; background: var(--ink); margin: 0 2px; }
  .badge {
    width: 59px; height: 59px; border-radius: 12px;
    background: var(--icon-dark); color: #e4e4e4;
    display: flex; align-items: center; justify-content: center; text-align: center;
    font: 600 17px/1 "Fira Sans", sans-serif;
  }
  .badge--large { font-size: 21px; }
  .badge--small { font-size: 14px; letter-spacing: -.3px; }
  .badge--stack { font-size: 15px; line-height: 1.02; }

  .info-zone__text {
    position: absolute; left: 0; right: 0; top: 114px;
    text-align: center;
    font: italic 400 21px/1.38 "Fira Sans", sans-serif; color: var(--ink);
  }
  .info-zone__text strong { font-weight: 800; }
  .info-zone__volume {
    position: absolute; left: 0; right: 0; top: 186px;
    text-align: center;
    font: 600 28px/1 "Fira Sans", sans-serif; color: var(--ink);
  }
</style>
</head>
<body>
  <main class="label">
    <section class="flavour-zone">
      <div class="flavour-zone__green"></div>
      <div class="flavour-panel">
        <p class="flavour-panel__claim">PROBIOTICS &amp; ENZYMES DETOX</p>
        <p class="flavour-panel__name">ginger brew</p>
        <p class="flavour-panel__desc">fermented green tea with<br>ginger-cinnamon-lime</p>
      </div>
    </section>

    <section class="brand-band">
      <h1 class="brand-band__name">VELMORA</h1>
      <span class="brand-band__rule brand-band__rule--left"></span>
      <p class="brand-band__sub">ZI</p>
      <span class="brand-band__rule brand-band__rule--right"></span>
    </section>

    <section class="info-zone">
      <div class="info-zone__center"></div>
      <div class="badge-row">
        <span class="badge-row__group-label">LOW</span>
        <span class="badge badge--large">GI</span>
        <span class="badge badge--large">Cal.</span>
        <span class="badge-row__divider"></span>
        <span class="badge-row__group-label">NO</span>
        <span class="badge badge--stack">Cane<br>Sugar</span>
        <span class="badge">Salt</span>
        <span class="badge badge--small">Lactose</span>
        <span class="badge badge--small">Coeliac</span>
      </div>
      <p class="info-zone__text">No artificial preservatives or colours<br><strong>100%</strong> Organic &amp; raw living culture</p>
      <p class="info-zone__volume">300 ml</p>
    </section>
  </main>
</body>
</html>
```